Marketing Skill "Workouts"; Design for an e-mail attachment highlighting Marketing training subjects

I am a freelance marketing trainer based in Singapore and need to e-mail out an attachment (probably saved as a PDF) to potential clients showing the training services I offer. These clients are all large blue-chip multinational companies so the attachment needs to look professional/high quality when opened on a computer.

My Company is called "Clearpath Marketing" (logo attached)

I am assuming the size should be A4 one sided colour.

I have attached some files that show best-attempts so far. These contain the key information, but the layouts all still look rather pedestrian. I am looking for something that looks a bit more dynamic but remains clear/easy to read.

Target Market(s)

HR/Marketing managers in multinational firms, mainly consumer goods

Industry/Entity Type

Marketing

Font styles to use
Sans Serif

Colors

Designer to choose colors to be used in the design.

Requirements
Must have
• Must look modern, up-to-date, professional.
Should not have
• Not gimmicky, like a cheap deal

```html
<!DOCTYPE html>
<html lang="en">
<head>
<meta charset="utf-8">
<title>Marketing skill "Workouts" – Clearpath Marketing</title>
<link rel="stylesheet" href="https://fonts.googleapis.com/css2?family=Ubuntu:ital,wght@0,500;0,700;1,500&family=Roboto+Condensed:wght@700&family=Open+Sans:wght@400;600;700&family=Ubuntu+Mono:wght@700&display=swap">
<style>
  :root {
    --brand-red: #9b1b1f;
    --brand-red-dark: #7d1418;
    --ink: #1e1e1e;
    --charcoal: #2d2d2f;
    --ring-grey: #e4e4e4;
    --white: #ffffff;
    --highlight: #f6d86a;
    --parchment-light: #f6ecd2;
    --parchment-dark: #e3cf9f;
    --rule-grey: #8a8886;
  }
  * { box-sizing: border-box; margin: 0; padding: 0; }
  html, body { width: 862px; height: 1200px; overflow: hidden; background: var(--white); }
  .flyer { position: relative; width: 862px; height: 1200px; background: var(--white); overflow: hidden; font-family: "Open Sans", sans-serif; color: var(--ink); }

  .hero-photo {
    position: absolute; left: 28px; top: 300px; width: 820px; height: 332px;
    background: linear-gradient(180deg, #ffffff 0%, #dfe8f3 22%, #b9c9dc 42%, #d8d36a 60%, #9ea3a8 76%, #c9cccf 100%);
  }

  .headline {
    position: absolute; left: 54px; top: 46px;
    font-family: "Ubuntu", sans-serif; font-weight: 700; font-size: 76px; line-height: 88px;
    color: var(--brand-red); letter-spacing: -1px;
  }
  .subhead {
    position: absolute; left: 56px; top: 238px; width: 540px;
    font-family: "Ubuntu", sans-serif; font-style: italic; font-weight: 500; font-size: 22px; line-height: 29px;
    color: #333;
  }

  .teaser-badge { position: absolute; left: 590px; top: 0; width: 272px; height: 310px; }
  .teaser-text {
    position: absolute; right: 62px; top: 58px; text-align: right;
    font-family: "Roboto Condensed", sans-serif; font-weight: 700; font-size: 56px; line-height: 54px;
    color: var(--white);
  }

  .web-tab { position: absolute; left: 28px; top: 584px; width: 470px; height: 60px; }
  .web-address {
    position: absolute; left: 86px; top: 590px;
    font-family: "Ubuntu Mono", monospace; font-weight: 700; font-size: 36px; color: var(--white);
  }

  .info-panel { position: absolute; left: 14px; top: 632px; width: 834px; height: 428px; background: var(--brand-red); }
  .column-rule { position: absolute; left: 421px; top: 676px; width: 1px; height: 168px; background: rgba(0,0,0,0.25); box-shadow: 1px 0 0 rgba(255,255,255,0.12); }

  .list-heading { position: absolute; font-family: "Open Sans", sans-serif; font-weight: 600; font-size: 26px; color: var(--white); }
  .topics-heading { left: 54px; top: 664px; }
  .benefits-heading { left: 462px; top: 664px; }

  .tick-list { position: absolute; list-style: none; color: var(--white); font-size: 13.6px; line-height: 23.2px; }
  .tick-list li { position: relative; padding-left: 22px; }
  .tick-list li::before {
    content: ""; position: absolute; left: 2px; top: 7px; width: 9px; height: 5px;
    border-left: 1.6px solid var(--white); border-bottom: 1.6px solid var(--white); transform: rotate(-45deg);
  }
  .topics-list { left: 54px; top: 710px; width: 360px; }
  .benefits-list { left: 463px; top: 708px; width: 360px; }
  .benefits-list li { line-height: 16.5px; margin-bottom: 6.7px; }

  .contact-lead { position: absolute; left: 57px; top: 952px; font-weight: 600; font-size: 19px; color: var(--highlight); }
  .contact-phone { position: absolute; left: 56px; top: 984px; font-family: "Roboto Condensed", sans-serif; font-weight: 700; font-size: 34px; color: var(--white); }
  .contact-email { position: absolute; left: 57px; top: 1022px; font-weight: 600; font-size: 20px; color: var(--white); letter-spacing: 0.3px; }

  .why-card {
    position: absolute; left: 466px; top: 862px; width: 342px; height: 204px;
    border: 4px solid #f2f2f2; box-shadow: 0 2px 6px rgba(0,0,0,0.35);
    background: radial-gradient(ellipse at 70% 40%, var(--parchment-light) 0%, var(--parchment-dark) 100%);
    padding: 12px 16px 0 18px; color: var(--ink);
  }
  .why-title { display: flex; align-items: center; gap: 10px; font-weight: 700; font-size: 26px; color: var(--brand-red); line-height: 32px; }
  .why-title::after { content: ""; flex: 1; height: 8px; background: var(--rule-grey); }
  .why-lead { margin-top: 12px; font-weight: 600; font-size: 14px; line-height: 19px; }
  .why-body { margin-top: 10px; font-size: 13.4px; line-height: 19px; }
  .why-body b { font-weight: 700; }

  .closing-line {
    position: absolute; left: 57px; top: 1070px;
    font-family: "Roboto Condensed", sans-serif; font-weight: 700; font-size: 43px; line-height: 46px;
    color: var(--brand-red);
  }

  .brand-mark { position: absolute; left: 578px; top: 1078px; display: flex; align-items: center; gap: 10px; }
  .brand-name { font-family: "Open Sans", sans-serif; font-weight: 600; font-size: 22px; color: var(--ink); }
  .brand-dot { width: 64px; height: 64px; border-radius: 50%; background: var(--brand-red); }
</style>
</head>
<body>
<main class="flyer">
  <div class="hero-photo" role="img" aria-label="Athletic man doing push-ups on kettlebells on a gym floor"></div>

  <h1 class="headline">Marketing skill<br>“Workouts”</h1>
  <p class="subhead">Problem solved with 1 day intensive workshops that willdrive business growth and motivate your team</p>

  <svg class="teaser-badge" viewBox="0 0 272 310" aria-hidden="true">
    <circle cx="148" cy="158" r="148" fill="var(--ring-grey)"/>
    <circle cx="148" cy="158" r="134" fill="var(--brand-red)"/>
    <rect x="258" y="0" width="14" height="310" fill="var(--white)"/>
  </svg>
  <p class="teaser-text">No<br>time to<br>learn?</p>

  <svg class="web-tab" viewBox="0 0 470 60" aria-hidden="true">
    <path d="M0 60 L40 10 Q48 0 62 0 L420 0 Q434 0 442 10 L470 60 Z" fill="var(--charcoal)"/>
  </svg>
  <p class="web-address">www.clearpath-marketing.com</p>

  <section class="info-panel" aria-label="Course details"></section>
  <div class="column-rule"></div>

  <h2 class="list-heading topics-heading">Key Topics:</h2>
  <ul class="tick-list topics-list">
    <li>Developing StrongBrand Plans</li>
    <li>Writing inspiring Briefs/Creative Evaluation</li>
    <li>Shopper Marketing/Developing Retail Promotions</li>
    <li>Brilliant Launch Management</li>
    <li>Improving Marketing R.O.I.</li>
    <li>Driving Brand Growth without Product Innovation</li>
    <li>Insight/Concept Development</li>
    <li>Integrating Digital Channels</li>
    <li>Creativity and Idea Generation</li>
  </ul>

  <h2 class="list-heading benefits-heading">Key Benefits:</h2>
  <ul class="tick-list benefits-list">
    <li>Latest in world-class thinking/tools/case studies</li>
    <li>Ability to “customize” toaddress your specific business issues</li>
    <li>Take-away “checklists” to embed behaviors and skills</li>
    <li>Asian context / relevance</li>
    <li>Proven quality</li>
  </ul>

  <p class="contact-lead">Please get in touch;</p>
  <p class="contact-phone">+65 9000 4417</p>
  <p class="contact-email">info@clearpath-marketing.com</p>

  <aside class="why-card">
    <h3 class="why-title">Why me?</h3>
    <p class="why-lead">The latest thinking, made PRACTICAL and ACTIONABLE.</p>
    <p class="why-body"><b>20 years of business experience</b> combined with over <b>10 years of proven training</b> / facilitation for major “blue-chip” clients, regularly scoring 90%+ satisfaction.</p>
  </aside>

  <p class="closing-line">World class quality<br>Without the costs</p>

  <div class="brand-mark">
    <span class="brand-name">Clearpath Marketing</span>
    <span class="brand-dot" aria-hidden="true"></span>
  </div>
</main>
</body>
</html>
```